Business Card Design Project

I need a business card design for my law office. I already have a logo.

I am an employment attorney who represents clients who have been wrongfully terminated or have been discriminated against by their employer.

I would like a unique, clean design using the colors in the logo or colors that complement the logo.

Target Market(s)

Clients, potential clients, other attorneys and others.

Industry/Entity Type

Attorney

Requirements
Must have
• I would like to use both sides of the card.

The information on the card must be easy to read.

Here is my information:

T. Dale Everhoff
3857 E. Pallister Rd., Suite 204
Harlow Springs, California 93650
559-731-4086
559-862-5143 fax
dale@lawtde.example
Nice to have
• QR Code? I would like to see designs incorporating a nice-looking QR code. Look at this example:

Notice the second QR code in the article - the color.

```html
<!DOCTYPE html>
<html lang="en">
<head>
<meta charset="utf-8">
<title>Everhoff Law Office – Business Card</title>
<link rel="stylesheet" href="https://fonts.googleapis.com/css2?family=EB+Garamond:wght@400;500;600&display=swap">
<style>
  :root {
    --page-bg: #1b1b1c;
    --card-white: #ffffff;
    --card-grey: #7a7b7d;
    --brand-blue: #1f8fd6;
    --ink-dark: #1d1d1f;
    --ink-mid: #55575b;
    --rule: #c9cbce;
    --on-grey: #f4f4f4;
  }
  * { box-sizing: border-box; margin: 0; padding: 0; }
  html, body { width: 1200px; height: 830px; overflow: hidden; }
  body {
    background: var(--page-bg);
    font-family: "EB Garamond", Georgia, serif;
    position: relative;
  }
  .card {
    position: absolute;
    top: 266px;
    width: 520px;
    height: 298px;
    border-radius: 3px;
    box-shadow: 0 10px 30px rgba(0,0,0,.5);
    overflow: hidden;
  }
  .card--front { left: 60px; background: var(--card-white); }
  .card--back {
    left: 620px;
    background: var(--card-grey);
    display: flex;
    align-items: center;
    justify-content: center;
  }
  .edge-band {
    position: absolute;
    width: 12px;
    background: var(--brand-blue);
  }
  .edge-band--left { left: 0; top: 0; height: 150px; }
  .edge-band--right { right: 0; bottom: 0; height: 90px; }

  .brand {
    position: absolute;
    left: 34px;
    top: 62px;
    display: flex;
    align-items: center;
    gap: 10px;
  }
  .brand__mark {
    width: 24px;
    height: 24px;
    background: var(--brand-blue);
  }
  .brand__name {
    font-size: 26px;
    font-weight: 500;
    color: var(--brand-blue);
    line-height: 1;
  }

  .holder {
    position: absolute;
    right: 32px;
    top: 32px;
    text-align: right;
  }
  .holder__name { font-size: 19px; font-weight: 600; color: var(--ink-dark); line-height: 1.1; }
  .holder__title { font-size: 13px; color: var(--ink-mid); }

  .address {
    position: absolute;
    left: 34px;
    top: 118px;
    font-style: normal;
    font-size: 14px;
    line-height: 1.3;
    color: var(--ink-mid);
  }
  .address__web { color: var(--brand-blue); font-weight: 500; }

  .divider {
    position: absolute;
    left: 262px;
    top: 124px;
    width: 1px;
    height: 96px;
    background: var(--rule);
  }

  .contacts {
    position: absolute;
    left: 280px;
    top: 150px;
    list-style: none;
    font-size: 14px;
    line-height: 1.35;
    color: var(--ink-mid);
  }
  .contacts li { display: flex; align-items: center; gap: 8px; }
  .contacts svg { width: 11px; height: 11px; fill: var(--brand-blue); flex: none; }

  .back__url {
    font-size: 40px;
    color: var(--on-grey);
    letter-spacing: .5px;
  }
</style>
</head>
<body>
  <section class="card card--front" aria-label="Card front">
    <span class="edge-band edge-band--left"></span>
    <span class="edge-band edge-band--right"></span>

    <div class="brand">
      <span class="brand__mark"></span>
      <span class="brand__name">Everhoff Law Office</span>
    </div>

    <div class="holder">
      <p class="holder__name">T. Dale Everhoff</p>
      <p class="holder__title">Operation Manager</p>
    </div>

    <address class="address">
      3857 E. Pallister Rd., Suite 204<br>
      Harlow Springs, California 93650<br>
      <span class="address__web">www.lawtde.example</span>
    </address>

    <span class="divider"></span>

    <ul class="contacts">
      <li>
        <svg viewBox="0 0 12 12" aria-hidden="true"><path d="M2.5 0.8l2 2.2-1 1.4c.7 1.6 2 2.9 3.6 3.6l1.4-1 2.2 2-1.2 1.9C5 10.6 1.4 7 .6 2z"/></svg>
        559-731-4086
      </li>
      <li>
        <svg viewBox="0 0 12 12" aria-hidden="true"><path d="M3 0h5l1 2v2H3zM1 5h10v5H9v2H3v-2H1zM4 8v3h4V8z"/></svg>
        559-862-5143
      </li>
      <li>
        <svg viewBox="0 0 12 12" aria-hidden="true"><path d="M0 2h12v8H0zM1 3l5 3.5L11 3z" fill-rule="evenodd"/></svg>
        dale@lawtde.example
      </li>
    </ul>
  </section>

  <section class="card card--back" aria-label="Card back">
    <p class="back__url">www.lawtde.example</p>
  </section>
</body>
</html>
```